Design the Mobile Version of Existing Web Based Health Platform

Loomcrest is a social business enterprise that focus on public health by applying innovative healthcare services and consumer internet technology. Loomcrest offers a personalized platform of health promotion and disease prevention that puts the individual back in control of his life.

Loomcrest is looking for a Mobile Web UX/Visual Design professional to create a mobile version of Loomcrest website platform for iPhone, iPad/tablet and Android.

Contestants must to check www.loomcrest-demo.com.br to have a better understanding of Loomcrest Platform by creating an account (it's in portuguese, but anyone can get the general idea).

The mobile version of Loomcrest should have very similar functionality and user flows. This job is not to reengineer or re-imagine Loomcrest. It is just to reformat the existing functionality so it works well on mobile devices.

This description below is to help you to understand the core features of the platform (check the attachments to see the new web design of each one):

- Personally Controlled Health Record - PCHR enables an individual to own and manage a complete, secure, digital copy of her health and wellness information.
- Health Risk Assessments - is a process to estimate the nature and probability of adverse health effects, based on personal and family historical data, behavior and environment.
- Simulation of future health - "what if analysis" that emphasizes health education and behavior change.
- Step Quests - a program that gives you the opportunity to the participant to advance his personal well-being by doing simple Step Quests
- Health Alerts and Recommendations and Missing Data - Recommendations based on Wellbeing Bureau Guidelines and Federal Wellness Review Panel (FWRP), plus notifications to update outdated information.

The deliverable for this project is a psd file with a designed mobile version of Loomcrest.

A new design of the web platform is under construction. You can also check it looking at the files attached.

Target Market(s)

people 25-40 years old, 60% female, socially engaged

Industry/Entity Type

Healthcare

Requirements
Must have
• iPhone, iPad and Android version

Design must cover all current functionalities available on the web version (please, ensure you understand all features by creating an account at www.loomcrest-demo.com.br)

- Login/Sign up
- Welcome (first assessment)
- Add to Personal Controlled Health Record (PCHR)
- Update/Remove PCHR
- List PCHR
- Riskgrid (risk assessmen results)
- Simulation
- Alerts
- Missing data
- Recommendations
- StepQuest
- Badges
- Configurations

It's important to check the attachments to see how the web platform design is evolving.

```html
<!DOCTYPE html>
<html lang="en">
<head>
<meta charset="utf-8">
<title>Loomcrest Mobile Menu</title>
<link rel="stylesheet" href="https://fonts.googleapis.com/css2?family=Roboto:wght@400&family=Source+Sans+3:wght@600;700&display=swap">
<style>
  :root {
    --page-bg: #f2f2f2;
    --brand-green: #9ccc3c;
    --accent-orange: #f39133;
    --accent-orange-deep: #ee6f1b;
    --menu-dark: #3c3c3c;
    --menu-darker: #2f2f2f;
    --menu-line: #333333;
    --menu-line-light: #474747;
    --text-light: #ffffff;
    --field-bg: #ffffff;
    --field-text: #8a8a8a;
    --underlay-grey: #dcdcdc;
    --underlay-white: #f7f7f7;
    --edit-btn: #555555;
    --avatar-tone: #7fa3b0;
  }
  * { box-sizing: border-box; margin: 0; padding: 0; }
  html, body {
    width: 864px; height: 1200px; overflow: hidden;
    background: var(--page-bg);
    font-family: "Source Sans 3", Arial, sans-serif;
  }
  .screen {
    position: absolute; left: 96px; top: 0;
    width: 672px; height: 1200px; overflow: hidden;
    background: var(--underlay-white);
  }
  .app-bar {
    position: absolute; left: 0; top: 0; width: 672px; height: 89px;
    background: var(--brand-green);
  }
  .menu-toggle {
    position: absolute; left: 26px; top: 21px; width: 54px; height: 46px;
    background: var(--field-bg); border-radius: 4px;
    display: flex; align-items: center; justify-content: center;
  }
  .underlay { position: absolute; left: 0; top: 89px; width: 100px; height: 1111px; }
  .underlay-top { position: absolute; left: 0; top: 0; width: 100px; height: 178px; background: var(--underlay-grey); }
  .underlay-tab {
    position: absolute; left: 0; top: 77px; width: 66px; height: 55px;
    background: var(--accent-orange-deep); color: var(--text-light);
    font-weight: 700; font-size: 22px; line-height: 55px; text-align: right; padding-right: 8px;
    border-radius: 0 3px 3px 0; overflow: hidden; white-space: nowrap;
  }
  .edit-card {
    position: absolute; left: 0; width: 66px; background: #fff;
    border: 1px solid #e2e2e2; border-left: none;
  }
  .edit-btn {
    position: absolute; left: 8px; width: 41px; height: 38px;
    background: var(--edit-btn); border-radius: 3px;
    display: flex; align-items: center; justify-content: center;
  }
  .nav-drawer {
    position: absolute; left: 100px; top: 89px; width: 572px; height: 1111px;
    background: linear-gradient(160deg, var(--menu-dark) 0%, #444 55%, var(--menu-darker) 100%);
  }
  .record-field {
    position: absolute; left: 40px; top: 30px; width: 489px; height: 54px;
    background: var(--field-bg); display: flex; align-items: center; justify-content: space-between;
    padding: 0 14px 0 20px;
    font-family: "Roboto", Arial, sans-serif; font-size: 17px; color: var(--field-text);
  }
  .drawer-divider { position: absolute; left: 0; width: 572px; height: 2px; background: var(--menu-line); border-bottom: 1px solid var(--menu-line-light); }
  .avatar { position: absolute; left: 40px; top: 150px; width: 105px; height: 95px; background: linear-gradient(180deg, #9a8b7c 0%, var(--avatar-tone) 100%); }
  .greeting {
    position: absolute; left: 174px; top: 181px; font-size: 28px; font-weight: 700; color: var(--text-light);
  }
  .greeting-hello { color: var(--brand-green); }
  .nav-list { position: absolute; left: 0; top: 276px; width: 572px; list-style: none; }
  .nav-item {
    position: relative; height: 85px; display: flex; align-items: center;
    border-bottom: 2px solid var(--menu-line);
    color: var(--text-light); font-size: 24px; font-weight: 600;
  }
  .nav-icon { width: 130px; display: flex; justify-content: center; padding-right: 18px; }
  .nav-item.is-active { background: var(--accent-orange); border-bottom-color: var(--accent-orange); }
  .nav-add {
    position: absolute; right: 0; top: 0; width: 92px; height: 85px; background: #fff;
    display: flex; align-items: center; justify-content: center;
  }
</style>
</head>
<body>
<div class="screen">
  <header class="app-bar">
    <div class="menu-toggle" aria-label="Menu">
      <svg width="34" height="24" viewBox="0 0 34 24"><rect y="1" width="34" height="4" rx="1" fill="#f39133"/><rect y="10" width="34" height="4" rx="1" fill="#f39133"/><rect y="19" width="34" height="4" rx="1" fill="#f39133"/></svg>
    </div>
  </header>

  <div class="underlay" aria-hidden="true">
    <div class="underlay-top"></div>
    <div class="underlay-tab">ner</div>
    <div class="edit-card" style="top:396px;height:169px;">
      <div class="edit-btn" style="top:21px;"><svg width="22" height="22" viewBox="0 0 22 22"><path d="M4 18l1-5L15 3l4 4L9 17z" fill="none" stroke="#fff" stroke-width="2"/></svg></div>
      <div class="edit-btn" style="top:106px;"><svg width="22" height="22" viewBox="0 0 22 22"><path d="M4 18l1-5L15 3l4 4L9 17z" fill="none" stroke="#fff" stroke-width="2"/></svg></div>
    </div>
    <div class="edit-card" style="top:687px;height:256px;">
      <div class="edit-btn" style="top:21px;"><svg width="22" height="22" viewBox="0 0 22 22"><path d="M4 18l1-5L15 3l4 4L9 17z" fill="none" stroke="#fff" stroke-width="2"/></svg></div>
      <div class="edit-btn" style="top:106px;"><svg width="22" height="22" viewBox="0 0 22 22"><path d="M4 18l1-5L15 3l4 4L9 17z" fill="none" stroke="#fff" stroke-width="2"/></svg></div>
      <div class="edit-btn" style="top:191px;"><svg width="22" height="22" viewBox="0 0 22 22"><path d="M4 18l1-5L15 3l4 4L9 17z" fill="none" stroke="#fff" stroke-width="2"/></svg></div>
    </div>
  </div>

  <nav class="nav-drawer">
    <div class="record-field">
      <span>Add a new record</span>
      <svg width="22" height="30" viewBox="0 0 22 30"><rect x="2" y="4" width="18" height="24" rx="2" fill="none" stroke="#333" stroke-width="2"/><rect x="7" y="1" width="8" height="6" rx="1" fill="#333"/><path d="M6 12h10M6 17h10M6 22h10" stroke="#333" stroke-width="2"/></svg>
    </div>
    <div class="drawer-divider" style="top:118px;"></div>
    <div class="avatar" role="img" aria-label="Profile photo of the signed-in user"></div>
    <p class="greeting"><span class="greeting-hello">Good Day,</span> Ravendi!</p>
    <ul class="nav-list">
      <li class="nav-item"><span class="nav-icon"><svg width="22" height="38" viewBox="0 0 22 38"><circle cx="11" cy="6" r="5" fill="none" stroke="#fff" stroke-width="2.5"/><path d="M3 22a8 8 0 0116 0v6a8 8 0 01-16 0z" fill="#fff"/></svg></span>Health Map</li>
      <li class="nav-item"><span class="nav-icon"><svg width="26" height="40" viewBox="0 0 26 40"><circle cx="13" cy="6" r="5" fill="#fff"/><path d="M5 14h16v14h-4v10h-8V28H5z" fill="#fff"/><path d="M9 20l4 4 4-4" stroke="#3c3c3c" stroke-width="2" fill="none"/></svg></span>Simulation</li>
      <li class="nav-item"><span class="nav-icon"><svg width="46" height="40" viewBox="0 0 46 40"><ellipse cx="15" cy="14" rx="14" ry="11" fill="#fff"/><path d="M6 22l-2 8 8-5z" fill="#fff"/><ellipse cx="31" cy="24" rx="13" ry="11" fill="#fff" stroke="#3c3c3c" stroke-width="2"/><path d="M9 14l5 5 8-9" stroke="#3c3c3c" stroke-width="3" fill="none"/><path d="M27 20l8 8M35 20l-8 8" stroke="#3c3c3c" stroke-width="3"/></svg></span>Challenges</li>
      <li class="nav-item is-active"><span class="nav-icon"><svg width="34" height="36" viewBox="0 0 34 36"><rect x="3" y="2" width="28" height="32" rx="2" fill="#fff"/><circle cx="18" cy="14" r="4" fill="#f39133"/><path d="M11 27a7 7 0 0114 0z" fill="#f39133"/><path d="M1 8h5M1 15h5M1 22h5M1 29h5" stroke="#f39133" stroke-width="2"/></svg></span>Booklet
        <span class="nav-add"><svg width="40" height="40" viewBox="0 0 40 40"><path d="M20 4v32M4 20h32" stroke="#f39133" stroke-width="6"/></svg></span>
      </li>
      <li class="nav-item"><span class="nav-icon"><svg width="38" height="36" viewBox="0 0 38 36"><path d="M9 2h20v10a10 10 0 01-20 0z" fill="#fff"/><path d="M9 5H2c0 7 3 10 8 11M29 5h7c0 7-3 10-8 11" stroke="#fff" stroke-width="2.5" fill="none"/><rect x="17" y="22" width="4" height="7" fill="#fff"/><rect x="11" y="29" width="16" height="5" fill="#fff"/><path d="M19 5l1.6 3.4 3.6.4-2.7 2.5.8 3.6-3.3-1.9-3.3 1.9.8-3.6-2.7-2.5 3.6-.4z" fill="#3c3c3c"/></svg></span>Trophies</li>
      <li class="nav-item"><span class="nav-icon"><svg width="34" height="34" viewBox="0 0 34 34" fill="#fff"><rect x="0" y="0" width="9" height="9"/><rect x="12" y="0" width="9" height="9"/><rect x="24" y="0" width="9" height="9"/><rect x="0" y="12" width="9" height="9"/><rect x="12" y="12" width="9" height="9"/><rect x="24" y="12" width="9" height="9"/><rect x="0" y="24" width="9" height="9"/><rect x="12" y="24" width="9" height="9"/><rect x="24" y="24" width="9" height="9"/></svg></span>More</li>
    </ul>
  </nav>
</div>
</body>
</html>
```